Elegant Financial Planning Business Card

Clearpath Wealth Advisory Pty Ltd requires an elegant business card that communicates simplicity, elegance and trust.
Attached card example of 'Varnoth' is very close to what I am looking for. Looking for black and white card.
Update 24/1/16: The attached Varnoth card is almost exactly what I am looking for. Although it is possible that alternative layouts may interest me, it is considerably more likely that I will proceed with a virtual clone of the "Varnoth' example.
Industry/Entity Type
Financial Planning
Contact Information for Business Card
In black font...
Front Details are (layout as per Dana Varnoth card picture):
Line1 - Name: Oliver Marsh
Line 2 - Company: Clearpath Wealth Advisory Pty Ltd
Line 3 - Address: Harbourview Plaza 3, Level 17, 58 Lomond Avenue, Marrowvale QLD
Line 4
- Phone: 136 712
- Email: advice@cpwa-example.com.au
- Site: www.cpwa-example.com.au
Back details
1/ logo in position and dimensions as per attached layout
2. Bottom left (in smaller writing).
- Authorised Representative No. 517946
- Clearpath Wealth Advisory is a corporate authorised representative of Tarquay7 Capital Services Pty Ltd
- ABN 47 318 602 154
- AFSL No. 608139

```html
<!DOCTYPE html>
<html lang="en">
<head>
<meta charset="utf-8">
<title>Clearpath Wealth Advisory – Business Card</title>
<link rel="stylesheet" href="https://fonts.googleapis.com/css2?family=Playfair+Display:wght@400;700&display=swap">
<style>
  :root {
    --bg: #e9e6e1;
    --ink: #0a0a0a;
    --paper: #ffffff;
    --paper-text: #111111;
    --front-text: #f2f2f2;
    --front-muted: #c9c9c9;
    --shadow: rgba(0, 0, 0, 0.18);
  }
  * { box-sizing: border-box; margin: 0; padding: 0; }
  html, body {
    width: 1200px;
    height: 700px;
    overflow: hidden;
    background: var(--bg);
    font-family: "Playfair Display", Georgia, serif;
  }
  .canvas {
    width: 1200px;
    height: 700px;
    display: flex;
    align-items: center;
    justify-content: center;
    gap: 60px;
  }
  .card {
    position: relative;
    width: 520px;
    height: 300px;
    box-shadow: 0 10px 26px var(--shadow);
  }
  /* Front */
  .card-front {
    background: var(--ink);
    color: var(--front-text);
    padding: 38px 40px;
  }
  .front-wordmark {
    font-size: 20px;
    font-weight: 700;
    color: var(--front-text);
    letter-spacing: 0.5px;
  }
  .front-details { margin-top: 34px; }
  .holder-name {
    font-size: 24px;
    font-weight: 400;
    letter-spacing: 0.5px;
  }
  .company-name {
    font-size: 11px;
    color: var(--front-muted);
    margin-top: 4px;
  }
  .address {
    font-size: 10.5px;
    color: var(--front-muted);
    margin-top: 14px;
  }
  .contact-list {
    list-style: none;
    margin-top: 22px;
    font-size: 10.5px;
    color: var(--front-muted);
  }
  .contact-list li {
    display: flex;
    align-items: center;
    gap: 8px;
    margin-bottom: 5px;
  }
  .contact-icon { width: 9px; height: 9px; flex: none; }
  .website {
    font-size: 10.5px;
    color: var(--front-muted);
    margin-top: 14px;
  }
  /* Back */
  .card-back {
    background: var(--paper);
    color: var(--paper-text);
  }
  .back-wordmark {
    position: absolute;
    right: 34px;
    top: 36px;
    font-size: 60px;
    font-weight: 700;
    line-height: 1;
    color: var(--paper-text);
  }
  .compliance {
    position: absolute;
    left: 36px;
    right: 34px;
    top: 150px;
  }
  .rep-number {
    font-size: 15px;
    font-weight: 700;
  }
  .rep-statement {
    font-size: 8.5px;
    margin-top: 6px;
    max-width: 280px;
    line-height: 1.4;
  }
  .registrations {
    position: absolute;
    right: 0;
    top: 26px;
    text-align: right;
    font-size: 8.5px;
    line-height: 1.5;
  }
</style>
</head>
<body>
<main class="canvas">
  <section class="card card-front" aria-label="Business card front">
    <div class="front-wordmark">Clearpath</div>
    <div class="front-details">
      <h1 class="holder-name">Oliver Marsh</h1>
      <p class="company-name">Clearpath Wealth Advisory Pty Ltd</p>
      <p class="address">Harbourview Plaza 3, Level 17, 58 Lomond Avenue, Marrowvale QLD</p>
      <ul class="contact-list">
        <li>
          <svg class="contact-icon" viewBox="0 0 10 10" aria-hidden="true"><circle cx="5" cy="5" r="5" fill="#f2f2f2"/></svg>
          <span>136 712</span>
        </li>
        <li>
          <svg class="contact-icon" viewBox="0 0 10 10" aria-hidden="true"><circle cx="5" cy="5" r="5" fill="#f2f2f2"/></svg>
          <span>advice@cpwa-example.com.au</span>
        </li>
      </ul>
      <p class="website">www.cpwa-example.com.au</p>
    </div>
  </section>

  <section class="card card-back" aria-label="Business card back">
    <div class="back-wordmark">Clearpath</div>
    <div class="compliance">
      <p class="rep-number">Authorised Representative No. 517946</p>
      <p class="rep-statement">Clearpath Wealth Advisory is a corporate authorised representative of Tarquay7 Capital Services Pty Ltd</p>
      <p class="registrations">ABN 47 318 602 154<br>AFSL No. 608139</p>
    </div>
  </section>
</main>
</body>
</html>
```